Heron Accord Business Card

Need a business card for my nonprofit, Heron Accord Inc. Heron Accord is a conflict resolution practice that offers services that help people resolve problems peacefully.

Got Conflict? Try Conflict Coaching. Initial consultation is complimentary

Marisol Daventry-Kuhl, PhD
Heron Accord Inc.
www.heronaccord-example.org
E: info@heronaccord-example.org
P: 555-318-4927

Would like the attached logo on it, as well as our slogan, which is Finding Calm Around the RoomĀ®

```html
<!DOCTYPE html>
<html lang="en">
<head>
<meta charset="utf-8">
<title>Heron Accord Business Card</title>
<link href="https://fonts.googleapis.com/css2?family=Roboto:wght@400;500&family=Work+Sans:wght@400;500&display=swap" rel="stylesheet">
<style>
  :root {
    --backdrop: #2e2e30;
    --card-white: #ffffff;
    --brand-red: #ec2d38;
    --brand-gold: #b8902c;
    --ink: #2b2b2b;
  }
  * { margin: 0; padding: 0; box-sizing: border-box; }
  html, body { width: 1200px; height: 930px; overflow: hidden; }
  body { background: var(--backdrop); position: relative; font-family: "Work Sans", sans-serif; }

  .card { position: absolute; width: 564px; height: 323px; box-shadow: 0 4px 14px rgba(0,0,0,.45); }
  .card--front { left: 318px; top: 125px; background: var(--card-white); }
  .card--back { left: 317px; top: 514px; background: var(--brand-red); }

  .wordmark { display: flex; align-items: center; gap: 8px; font-family: "Work Sans", sans-serif; font-weight: 500; letter-spacing: .04em; white-space: nowrap; }
  .wordmark__dot { display: inline-block; border-radius: 50%; }

  .card--front .wordmark { position: absolute; right: 24px; top: 34px; font-size: 34px; color: var(--brand-gold); }
  .card--front .wordmark__dot { width: 22px; height: 22px; background: var(--brand-gold); }

  .holder { position: absolute; left: 21px; top: 175px; }
  .holder__name { font-family: "Roboto", sans-serif; font-weight: 500; font-size: 18px; color: var(--brand-red); }
  .holder__role { font-size: 14px; color: var(--ink); margin-top: 2px; }

  .divider { position: absolute; left: 21px; right: 24px; top: 226px; height: 1.5px; background: var(--brand-red); }

  .contacts { position: absolute; left: 21px; top: 247px; list-style: none; font-size: 14px; color: var(--ink); line-height: 18.5px; }
  .contacts li { display: flex; align-items: center; gap: 8px; }
  .contacts svg { width: 9px; height: 9px; flex: none; }
  .contacts .accent { color: var(--brand-red); }

  .address { position: absolute; right: 24px; top: 265px; text-align: right; font-size: 14px; line-height: 18.5px; color: var(--ink); font-style: normal; }

  .card--back .wordmark { position: absolute; left: 0; right: 0; top: 50%; transform: translateY(-50%); justify-content: center; font-size: 44px; color: var(--card-white); }
  .card--back .wordmark__dot { width: 28px; height: 28px; background: var(--card-white); }
</style>
</head>
<body>
  <section class="card card--front" aria-label="Business card front">
    <div class="wordmark"><span class="wordmark__dot"></span>Heron Accord</div>

    <div class="holder">
      <h1 class="holder__name">Marisol Daventry-Kuhl, PhD</h1>
      <p class="holder__role">President</p>
    </div>

    <div class="divider"></div>

    <ul class="contacts">
      <li>
        <svg viewBox="0 0 10 10"><path d="M2 1 L4 1 L4.6 3 L3.5 4 Q4.5 6 6 6.5 L7 5.4 L9 6 L9 8 Q8 9 6.5 8.8 Q2 7.5 1.2 3 Q1 1.8 2 1Z" fill="var(--brand-red)"/></svg>
        555-318-4927
      </li>
      <li>
        <svg viewBox="0 0 10 10"><rect x="0.8" y="2" width="8.4" height="6" fill="none" stroke="var(--brand-red)" stroke-width="1.2"/><path d="M1 2.5 L5 5.5 L9 2.5" fill="none" stroke="var(--brand-red)" stroke-width="1.2"/></svg>
        info@heronaccord-example.org
      </li>
      <li>
        <svg viewBox="0 0 10 10"><circle cx="5" cy="5" r="4" fill="none" stroke="var(--brand-red)" stroke-width="1"/><path d="M1 5 H9 M5 1 V9 M2 3 H8 M2 7 H8" stroke="var(--brand-red)" stroke-width=".8"/></svg>
        <span>www.<span class="accent">heronaccord-example</span>.org</span>
      </li>
    </ul>

    <address class="address">480 Alder Row, suite 12,<br>Riverton, CA 95000</address>
  </section>

  <section class="card card--back" aria-label="Business card back">
    <div class="wordmark"><span class="wordmark__dot"></span>Heron Accord</div>
  </section>
</body>
</html>
```